PowerPoint Design Project

We are looking for a corporate presentation design (example content provided on approximately 30 slides).

The design will be a corporate design for our brand: GVRU
Continental Voyage Planners Union
For brand colours, requirements and logo look at: www.gvru-sample.org/media
or check the attached documents. We need to incorporate logo and brand but we are happy to refresh the palette. Attached please also find designs and colour palette of our new website-presentation should complement these.

You are also free to use photos from events some of which can be found here:
http://www.socialpage-example.com/pages/Continental-Voyage-Planners-Union/507194362810935?sk=photos_stream

Most important:
-PROFESSIONAL AUDIENCE-PROFESSIONAL DESIGN
-SIMPLE (see example our homepage in attachment)
-ADDED SIMPLE ANIMATIONS

-DESIGN TO BE DONE ON THE EXAMPLE PRESENTATION BUT TO BE RE-USABLE FOR OTHER PRESENTATIONS
Updates

Hi, we have just uploaded our corporate social media icons which could be added on contact/end slide and on the welcome slide.

Hi all, 

-I uploaded a new high res version of the map which can be included in your designs (feel free to change colour scheme)
-Also amended upload of the Google + social media icon

Reason: I am looking forward to seeing a couple more designs. Please try including some suggested animations.

Target Market(s)

Presentation will be B2B and most audience are representatives of various companies in the tourism industry (tour operators, tourist boards, hotels )

Industry/Entity Type

Events

Requirements
Must have
• sleek graphics design
Nice to have
• animations

```html
<!DOCTYPE html>
<html lang="en">
<head>
<meta charset="utf-8">
<title>GVRU – Project Slide</title>
<link rel="stylesheet" href="https://fonts.googleapis.com/css2?family=Carlito:wght@400;700&family=Roboto+Condensed:wght@700&display=swap">
<style>
  :root {
    --band-navy: #1d2a55;
    --tab-navy: #0e1333;
    --page-white: #ffffff;
    --surface-grey: #e4e4e5;
    --surface-light: #f7f7f7;
    --pattern-grey: #d6d6d8;
    --map-grey: #dadadc;
    --rule-blue: #9aa3bd;
    --ink: #111111;
    --title-white: #ffffff;
  }
  * { margin: 0; padding: 0; box-sizing: border-box; }
  html, body {
    width: 1200px;
    height: 900px;
    overflow: hidden;
    background: var(--page-white);
  }
  .slide {
    position: relative;
    width: 1200px;
    height: 900px;
    overflow: hidden;
    background: linear-gradient(180deg, var(--surface-grey) 0%, var(--surface-light) 75%, var(--page-white) 100%);
    font-family: "Carlito", "Calibri", sans-serif;
  }
  .halftone-area {
    position: absolute;
    left: 0;
    top: 172px;
    width: 560px;
    height: 500px;
    background: radial-gradient(ellipse at 20% 30%, var(--pattern-grey) 0%, rgba(214,214,216,0.5) 40%, rgba(228,228,229,0) 75%);
  }
  .map-area {
    position: absolute;
    left: 670px;
    top: 190px;
    width: 530px;
    height: 630px;
    background: radial-gradient(ellipse at 55% 45%, var(--map-grey) 0%, rgba(218,218,220,0.55) 45%, rgba(240,240,240,0) 78%);
  }
  .header-band {
    position: absolute;
    left: 0;
    top: 0;
    width: 1200px;
    height: 172px;
    background: var(--band-navy);
  }
  .brand-tab {
    position: absolute;
    left: 90px;
    top: 0;
    width: 252px;
    height: 383px;
  }
  .brand-name {
    position: absolute;
    left: 90px;
    top: 128px;
    width: 252px;
    text-align: center;
    font-family: "Carlito", "Calibri", sans-serif;
    font-weight: 400;
    font-size: 40px;
    line-height: 1;
    color: var(--title-white);
  }
  .project-title {
    position: absolute;
    left: 387px;
    top: 70px;
    font-size: 47px;
    font-weight: 400;
    color: var(--title-white);
    line-height: 1;
  }
  .intro {
    position: absolute;
    left: 390px;
    top: 461px;
    width: 650px;
    font-size: 21px;
    line-height: 36px;
    color: var(--ink);
  }
  .intro span { display: block; white-space: nowrap; }
  .footer-rule {
    position: absolute;
    left: 0;
    top: 819px;
    width: 1200px;
    height: 2px;
    background: var(--rule-blue);
  }
  .page-number {
    position: absolute;
    left: 36px;
    top: 842px;
    font-family: "Roboto Condensed", "Arial Narrow", sans-serif;
    font-weight: 700;
    font-size: 24px;
    color: var(--ink);
  }
</style>
</head>
<body>
  <main class="slide">
    <div class="halftone-area" role="img" aria-label="Soft grey halftone dot pattern"></div>
    <div class="map-area" role="img" aria-label="Dotted map of Europe in pale grey"></div>

    <header class="header-band"></header>

    <svg class="brand-tab" viewBox="0 0 252 383" aria-hidden="true">
      <polygon points="0,0 252,0 252,300 0,383" fill="var(--tab-navy)"/>
    </svg>
    <div class="brand-name">GVRU</div>

    <h1 class="project-title">PROJECT TITLE HERE</h1>

    <p class="intro">
      <span>Some introduction content here Some introduction content</span>
      <span>hereSome introduction content hereSome introduction content</span>
      <span>here Some introduction content hereSome introduction content</span>
      <span>here</span>
    </p>

    <div class="footer-rule"></div>
    <div class="page-number">Page : 06</div>
  </main>
</body>
</html>
```